Banner for home page on event planning site

We are revamping the home page www.coralbellecelebrations.com and would like to add a banner to the center of it to guide potential clients to one of 3 areas of the site:

Weddings, Corporate Events, Parties and More

I'm uploading an attachment that shows where the banner will be placed. It needs to have those 3 distinct sections, and match the existing colors/branding of the site. The fonts used for the logo are Lucida Bright and Callie Hand. Both are available for free.

Please use lorem ipsum under each section, I'll fill that in later. It should just be highly designed, beautiful, and easy to understand that clicking these will take you to the different areas of the site.
Updates

Hi designers,
Here are some problems we are having with the designs that have been submitted.
1) 3 stock images as squares... when you do this and then put it into the existing website, it gets lost among the other boxes. We need this to be where the eye goes immediately when you land on the site.
2) Not enough of a frame or white space... we think you need some white space to make this stand out as different from the surrounding area.
3) No clearly defined areas. It needs to be easy for people to figure out... Weddings, click here. Parties, click here. Corporate events, click here.

Industry/Entity Type

Event Planning

Requirements
Should not have
• Nothing with orchids, her competitor uses them and they are common in the event planning industry. We want to stay away from them.

Files

```html
<!DOCTYPE html>
<html lang="en">
<head>
<meta charset="utf-8">
<title>Coral Belle Celebrations – Event Areas Banner</title>
<link rel="stylesheet" href="https://fonts.googleapis.com/css2?family=Crimson+Text&family=Parisienne&display=swap">
<style>
  :root {
    --berry: #b34e8c;
    --berry-deep: #a23f7c;
    --swirl: #d9a3c6;
    --swirl-light: #e8bde0;
    --heading: #c0508f;
    --panel: #ffffff;
    --ink: #1f1f1f;
  }
  * { margin: 0; padding: 0; box-sizing: border-box; }
  html, body {
    width: 1200px;
    height: 1000px;
    overflow: hidden;
    background: var(--berry);
  }
  .banner {
    position: relative;
    width: 1200px;
    height: 1000px;
    background: var(--berry);
    overflow: hidden;
  }
  .swirl-backdrop {
    position: absolute;
    inset: 0;
    background:
      radial-gradient(circle at 300px 230px, var(--swirl) 0 8%, transparent 28%),
      radial-gradient(circle at 560px 560px, var(--swirl) 0 6%, transparent 26%),
      radial-gradient(circle at 1030px 300px, var(--swirl-light) 0 6%, transparent 24%),
      linear-gradient(135deg, var(--berry) 0%, var(--berry-deep) 100%);
  }
  .area {
    position: absolute;
    top: 22px;
    height: 956px;
    background: var(--panel);
    display: block;
    color: var(--ink);
    text-decoration: none;
  }
  .area--weddings  { left: 20px;  width: 367px; }
  .area--corporate { left: 407px; width: 383px; }
  .area--parties   { left: 812px; width: 368px; }

  .area__title {
    font-family: "Parisienne", cursive;
    font-weight: 400;
    font-size: 62px;
    line-height: 100px;
    letter-spacing: 3px;
    color: var(--heading);
    text-align: center;
    padding-top: 12px;
  }
  .area--weddings .area__title { height: 172px; }
  .area--corporate .area__title,
  .area--parties .area__title { height: 192px; }

  .area__copy {
    font-family: "Crimson Text", Georgia, serif;
    font-size: 14px;
    line-height: 19.2px;
  }
  .area--weddings .area__copy  { padding: 8px 0 0 15px; }
  .area--corporate .area__copy { padding: 8px 0 0 25px; }
  .area--parties .area__copy   { padding: 8px 0 0 18px; }
  .area__copy p { margin-bottom: 19.2px; }
</style>
</head>
<body>
<main class="banner">
  <div class="swirl-backdrop" role="img" aria-label="Flowing pink swirl ornaments on a berry background"></div>

  <a class="area area--weddings" href="#weddings">
    <h2 class="area__title">Weddings</h2>
    <div class="area__copy">
      <p>Lorem ipsum dolor sit amet,<br>an bonorum percipit expetendis sit.<br>Natum choro consectetuer ei nam,<br>et eum tale dicit aliquando. Semper<br>delectus sed ei. Mazim facete ad mei,<br>ei dico doctus vel, facilis eloquentiam<br>eu per. Ex vide omnis interesset quo, sint<br>epicuri cum ex.</p>
      <p>Vix probo facete malorum eu, id reque<br>diceret pro. Noster eirmod comprehensam<br>eum id, est te graeco feugait. Cu eam<br>equidem epicuri necessitatibus. Graecis<br>fabellas corrumpit sea eu. Usu eu quod<br>scriptorem. Ex modus fabellas usu,<br>phaedrum similique intellegam sit te.</p>
      <p>Nominati eloquentiam sea in. Cu nonumy<br>atomorum delicata pro. Mei possit definitiones<br>ut, iudicabit moderatius id quo. Ius ne error<br>persecuti, dico gloriatur ex nec. Mei summo<br>aliquid id, eu tale oblique liberavisse quo.<br>Mea fugit scribentur theophrastus cu.</p>
      <p>Eum officiis splendide definitiones at.<br>No mei congue consulatu neglegentur,<br>aperiri malorum sit eu, qui ea feugiat assentior.<br>Ut pri vero ornatus dolorum. No purto facilisis<br>iracundia vim, decore legimus nam no. Est vidit<br>utinam ea. Vis ex homero quodsi tractatos.</p>
      <p>Eam facer postulant et. Id tantas vocent vis,<br>doming diceret accumsan mea ad. Eum no<br>aeque appetere nominati, ex mei integre periculis.<br>Erant solet reprimique pro ut, eu virtute accommodare<br>his. At viris facilisi mel, his omnis partem elaboraret cu.<br>Ut perfecto facilisis sed. Cum scaevola corrumpit at,<br>eum invenire conclusionemque no, sed quaeque<br>consetetur eu.</p>
    </div>
  </a>

  <a class="area area--corporate" href="#corporate-events">
    <h2 class="area__title">Corporate<br>Events</h2>
    <div class="area__copy">
      <p>Lorem ipsum dolor sit amet,<br>an bonorum percipit expetendis sit.<br>Natum choro consectetuer ei nam,<br>et eum tale dicit aliquando. Semper<br>delectus sed ei. Mazim facete ad mei,<br>ei dico doctus vel, facilis eloquentiam<br>eu per. Ex vide omnis interesset quo, sint<br>epicuri cum ex.</p>
      <p>Vix probo facete malorum eu, id reque<br>diceret pro. Noster eirmod comprehensam<br>eum id, est te graeco feugait. Cu eam<br>equidem epicuri necessitatibus. Graecis<br>fabellas corrumpit sea eu. Usu eu quod<br>scriptorem. Ex modus fabellas usu,<br>phaedrum similique intellegam sit te.</p>
      <p>Nominati eloquentiam sea in. Cu nonumy<br>atomorum delicata pro. Mei possit definitiones<br>ut, iudicabit moderatius id quo. Ius ne error<br>persecuti, dico gloriatur ex nec. Mei summo<br>aliquid id, eu tale oblique liberavisse quo.<br>Mea fugit scribentur theophrastus cu.</p>
      <p>Eum officiis splendide definitiones at.<br>No mei congue consulatu neglegentur,<br>aperiri malorum sit eu, qui ea feugiat assentior.<br>Ut pri vero ornatus dolorum. No purto facilisis<br>iracundia vim, decore legimus nam no. Est vidit<br>utinam ea. Vis ex homero quodsi tractatos.</p>
      <p>Eam facer postulant et. Id tantas vocent vis,<br>doming diceret accumsan mea ad. Eum no<br>aeque appetere nominati, ex mei integre periculis.<br>Erant solet reprimique pro ut, eu virtute accommodare<br>his. At viris facilisi mel, his omnis partem elaboraret cu.<br>Ut perfecto facilisis sed. Cum scaevola corrumpit at,<br>eum invenire conclusionemque no, sed quaeque<br>consetetur eu.</p>
    </div>
  </a>

  <a class="area area--parties" href="#parties">
    <h2 class="area__title">Parties<br>and More</h2>
    <div class="area__copy">
      <p>Lorem ipsum dolor sit amet,<br>an bonorum percipit expetendis sit.<br>Natum choro consectetuer ei nam,<br>et eum tale dicit aliquando. Semper<br>delectus sed ei. Mazim facete ad mei,<br>ei dico doctus vel, facilis eloquentiam<br>eu per. Ex vide omnis interesset quo, sint<br>epicuri cum ex.</p>
      <p>Vix probo facete malorum eu, id reque<br>diceret pro. Noster eirmod comprehensam<br>eum id, est te graeco feugait. Cu eam<br>equidem epicuri necessitatibus. Graecis<br>fabellas corrumpit sea eu. Usu eu quod<br>scriptorem. Ex modus fabellas usu,<br>phaedrum similique intellegam sit te.</p>
      <p>Nominati eloquentiam sea in. Cu nonumy<br>atomorum delicata pro. Mei possit definitiones<br>ut, iudicabit moderatius id quo. Ius ne error<br>persecuti, dico gloriatur ex nec. Mei summo<br>aliquid id, eu tale oblique liberavisse quo.<br>Mea fugit scribentur theophrastus cu.</p>
      <p>Eum officiis splendide definitiones at.<br>No mei congue consulatu neglegentur,<br>aperiri malorum sit eu, qui ea feugiat assentior.<br>Ut pri vero ornatus dolorum. No purto facilisis<br>iracundia vim, decore legimus nam no. Est vidit<br>utinam ea. Vis ex homero quodsi tractatos.</p>
      <p>Eam facer postulant et. Id tantas vocent vis,<br>doming diceret accumsan mea ad. Eum no<br>aeque appetere nominati, ex mei integre periculis.<br>Erant solet reprimique pro ut, eu virtute accommodare<br>his. At viris facilisi mel, his omnis partem elaboraret cu.<br>Ut perfecto facilisis sed. Cum scaevola corrumpit at,<br>eum invenire conclusionemque no, sed quaeque<br>consetetur eu.</p>
    </div>
  </a>
</main>
</body>
</html>
```